We sincerely appreciate everyone's interest in our website design project. In all we had 65 designs submitted and were amazed by the creativity and quality presented. Unfortunately, as with all contests, there can only be one winner and the winning firm was selected at 12:00 ET 7/7/2017. We wish you all the best and look forward to potentially working with you on future projects. Thanks again for your time and interests. Tobin

Thanks for your interest in our project! Due to the overwhelming number of submissions received, additional submissions will not be accepted after close of business 7/4. Additionally, to minimize unnecessary additional work, we will begin reviewing all submissions received on 7/5, select the submission(s) that come closest to meeting our needs and work with the designer(s) selected to finalize their designs. Thanks again.

Thanks for the feedback!!

Based on feedback provided, we understand that the initial specifications required that the site be developed as dynamic versus static and, as such, the budget was insufficient. With this in mind, we have modified the specifications as follows:
1. Clean, simple, uncluttered site
2. 4-5 pages consisting of the following:
a. Home page
b. About us
c. Services provided
d. Contact us/request quote/request service
2. No people in pools/photos unless it involves cleaning i.e., vacuuming, netting, etc.

We are in need of a website to promote our business and the services provided to our customers. The site should be a simple 5 page design providing information about us, the services we provide, our service territory (Central Florida = Seminole and Orange Counties), the ability to request a service quote, the ability to schedule service, the ability to pay invoices, the ability to refer neighbors and friends, the ability to leave reviews and provide feedback, etc. We are a certified, licensed, and insured veteran minority owned and operated company with 10 years industry experience providing unparalleled commercial and residential pool and spa care in the central Florida area. While we are seeking something more impressive and concise, an example of the site would be http://marlowpoolservice.example/ OR http://www.bluefinchpoolcompany.example/

Target Market(s)

Hotels, motels, apartment complexes, condominium associations, homeowners associations, and individual homeowners

Industry/Entity Type

It Company

Contact Information for Business Card

Logo, name, phone number, website, "Certified Licensed Insured", "Providing quality pool care to Central Florida"

Coding

Coded - Design and coding required

Number of Pages Required

5+ page

Requirements
Must have
• See description
Nice to have
• See description
Should not have
• See description

```html
<!DOCTYPE html>
<html lang="en">
<head>
<meta charset="utf-8">
<title>Sunway Pool Care</title>
<link rel="stylesheet" href="https://fonts.googleapis.com/css2?family=Open+Sans:wght@400;600;700&display=swap">
<style>
:root{
  --blue:#3f7dc0;
  --blue-dark:#2f65a8;
  --blue-light:#4f95d4;
  --orange:#f5a623;
  --yellow:#f4b942;
  --ink:#333a44;
  --muted:#6b717a;
  --soft-bg:#f5f5f5;
  --white:#ffffff;
  --footer-a:#4b5462;
  --footer-b:#5f6671;
  --line:#d9dde2;
}
*{box-sizing:border-box;margin:0;padding:0}
html,body{width:1200px;height:3243px;overflow:hidden}
body{position:relative;background:var(--white);font-family:"Open Sans",Arial,sans-serif;color:var(--ink)}
.abs{position:absolute}
.brand{font-weight:700;font-size:30px;color:var(--blue-dark);letter-spacing:-.5px;display:flex;align-items:center;gap:10px}
.brand-dot{width:14px;height:14px;border-radius:50%;background:var(--blue-dark)}
.btn{position:absolute;display:flex;align-items:center;justify-content:center;font-size:11px;font-weight:700;letter-spacing:.6px;text-transform:uppercase}
.btn-solid{background:var(--blue);color:var(--white)}
.btn-ghost{border:2px solid var(--white);color:var(--white)}
.social{display:flex;gap:8px}
.social span{width:30px;height:30px;border-radius:50%;background:#a9adb3;display:block}
.nav{display:flex;gap:22px;font-size:11px;font-weight:600;color:var(--ink);align-items:center}
.nav .home{width:12px;height:11px;background:var(--blue);clip-path:polygon(50% 0,100% 50%,85% 50%,85% 100%,15% 100%,15% 50%,0 50%)}
.hero-text h1{font-size:30px;font-weight:600;color:var(--white)}
.hero-text p{font-size:17px;color:var(--white);line-height:1.45;width:600px;margin-top:4px}
.dots{display:flex;gap:8px}
.dots i{width:8px;height:8px;border-radius:50%;border:1.5px solid var(--blue-light);display:block}
.dots i.on{background:var(--blue-light)}
.section-title{position:absolute;left:0;width:1200px;text-align:center;font-size:24px;font-weight:600;color:var(--ink)}
.tile{position:absolute;display:flex;flex-direction:column;align-items:center;justify-content:center;color:var(--white);font-weight:600;font-size:15px;text-align:center;line-height:1.3;text-shadow:0 1px 3px rgba(0,0,0,.5)}
.tile .btn{position:static;margin-top:14px;width:122px;height:32px;text-shadow:none}
.about p{font-size:12.5px;line-height:1.65;color:var(--muted);width:420px;margin-bottom:18px}
.booking{position:absolute;left:688px;top:1436px;width:280px;height:488px;background:var(--white);box-shadow:0 6px 24px rgba(0,0,0,.22)}
.booking-head{height:116px;background:linear-gradient(var(--blue-light),var(--blue-dark));color:var(--white);font-size:24px;font-weight:600;text-align:center;line-height:1.25;display:flex;align-items:center;justify-content:center}
.field{position:absolute;left:23px;width:232px;height:31px;border:1px solid var(--line);font-size:11px;color:#9aa0a8;padding:8px 10px}
.send{position:absolute;left:23px;top:423px;width:232px;height:35px;background:linear-gradient(var(--blue-light),var(--blue-dark));color:var(--white);font-size:11px;font-weight:700;display:flex;align-items:center;justify-content:center;gap:8px}
.testimonials{position:absolute;left:0;top:1896px;width:1200px;height:551px;background:linear-gradient(var(--blue-light),var(--blue-dark))}
.quote{position:absolute;left:270px;top:143px;width:660px;text-align:center;color:var(--white);font-size:15.5px;line-height:1.42}
.avatar{position:absolute;border-radius:50%;background:linear-gradient(#c9ced4,#7d8590);border:3px solid rgba(255,255,255,.7)}
.photo{position:absolute;top:2564px;width:232px;height:229px}
.footer-col h4{font-size:14px;font-weight:700;color:var(--white);margin-bottom:20px}
.footer-col li{list-style:none;font-size:12px;color:#e4e7eb;height:24px}
.footer-col li.active{color:var(--blue-light)}
.footer-col .big{font-size:20px;font-weight:600;color:var(--white)}
</style>
</head>
<body>

<!-- Header -->
<div class="abs brand" style="left:155px;top:40px">Sunway Pool Care</div>
<div class="abs" style="left:469px;top:48px;font-size:14px;color:var(--ink)">Call Us Today! <svg width="14" height="14" viewBox="0 0 24 24" style="vertical-align:-2px"><circle cx="12" cy="12" r="11" fill="none" stroke="var(--orange)" stroke-width="2"/><path d="M8 6c-1 1-1 3 1 6s4 5 6 5l2-2-2-2-2 1c-1-1-3-3-3-4l1-2-2-2z" fill="var(--orange)"/></svg> <b style="color:var(--orange);font-weight:600">407.555.0142</b></div>
<div class="btn btn-solid" style="left:735px;top:46px;width:167px;height:28px">Book a free quote</div>
<div class="abs social" style="left:934px;top:44px"><span></span><span style="background:var(--blue-light)"></span><span></span></div>

<!-- Hero -->
<svg class="abs" style="left:0;top:0" width="1200" height="770" viewBox="0 0 1200 770">
  <defs>
    <linearGradient id="heroFill" x1="0" y1="0" x2="0.6" y2="1">
      <stop offset="0" stop-color="#8f8a72"/>
      <stop offset=".35" stop-color="#b59a7a"/>
      <stop offset=".55" stop-color="#2d86b8"/>
      <stop offset=".8" stop-color="#1d6f9f"/>
      <stop offset="1" stop-color="#c9b39a"/>
    </linearGradient>
  </defs>
  <path role="img" aria-label="Photo of a backyard pool with stone deck, fountain wall and desert garden" d="M0 90 H1200 V757 C1050 760 900 700 700 640 C500 570 250 560 0 650 Z" fill="url(#heroFill)"/>
  <path d="M0 0 H1200 V97 C1000 95 850 100 720 150 C500 240 150 250 0 130 Z" fill="var(--white)"/>
  <line x1="151" y1="125" x2="588" y2="125" stroke="var(--line)"/>
</svg>
<div class="abs nav" style="left:151px;top:168px"><span class="home"></span><span>ABOUT US</span><span>SERVICES</span><span>CONTACT US</span></div>
<div class="abs hero-text" style="left:231px;top:420px">
  <h1>With 10 years industry experience</h1>
  <p>providing unparalleled commercial and residential pool and spa care in the central Florida area</p>
</div>
<div class="btn btn-ghost" style="left:231px;top:538px;width:137px;height:37px">Explore more</div>
<div class="abs dots" style="left:880px;top:677px"><i class="on"></i><i></i><i></i><i></i><i></i><i></i></div>

<!-- Services -->
<div class="abs" style="left:0;top:700px;width:1200px;height:766px;background:var(--soft-bg);z-index:-1"></div>
<svg class="abs" style="left:0;top:640px" width="1200" height="130" viewBox="0 0 1200 130"><path d="M0 10 C250 -80 500 -70 700 0 S1050 120 1200 117 V130 H0 Z" fill="var(--soft-bg)"/></svg>
<h2 class="section-title" style="top:806px">Serving Our Customers</h2>
<div class="tile" role="img" aria-label="Photo of a commercial swimming pool" style="left:231px;top:867px;width:281px;height:238px;background:linear-gradient(#8fb0d6,#2f6fb5)">Commercial Pool<br>Services<span class="btn btn-ghost">Learn more</span></div>
<div class="tile" role="img" aria-label="Photo of a residential pool at sunset" style="left:536px;top:867px;width:432px;height:238px;background:linear-gradient(#9a8f8a,#4e7d6a 55%,#5aa5c9)">Residential Pool<br>Services</div>
<div class="tile" role="img" aria-label="Photo of a hot tub on a wooden deck by the water" style="left:231px;top:1131px;width:433px;height:238px;background:linear-gradient(90deg,#4a2a20,#8a5a40 50%,#6d8ea8)">Spas &amp; Hot Tubs<br>Care</div>
<div class="tile" style="left:688px;top:1131px;width:280px;height:238px;background:var(--yellow);text-shadow:none">Request<br>A Service Quote</div>

<!-- About -->
<div class="abs brand" style="left:231px;top:1538px">Sunway Pool Care</div>
<div class="abs about" style="left:231px;top:1606px">
  <p>We are a certified, licensed, and insured veteran minority owned and operated company with 10 years industry experience providing unparalleled commercial and residential pool and spa care in the central Florida area.</p>
  <p>Lorem Ipsum is simply dummy text of the printing and typesetting industry. Lorem Ipsum has been the industry's standard dummy text ever since the 1500s, when an unknown printer ...</p>
</div>
<div class="btn btn-solid" style="left:231px;top:1794px;width:137px;height:33px">Discover more</div>

<!-- Testimonials -->
<div class="testimonials">
  <h2 class="section-title" style="top:88px;color:var(--white)">What Our Customers Are Saying</h2>
  <p class="quote">“ Sunway Pool Care is the only one we will let work on our pool, due that he is truly the best at his job and an honest good person. The amount of time and attention to detail he employs on servicing our pool twice a week is without a doubt the best service we received. We highly recommend asking for Sunway Pool Care and we hope this helps others be as happy as we are with our pool. Sincerely, Dana. ”</p>
  <svg class="abs" style="left:400px;top:326px" width="24" height="14" viewBox="0 0 24 14"><path d="M23 7H2M8 1L2 7l6 6" fill="none" stroke="rgba(255,255,255,.6)" stroke-width="2"/></svg>
  <svg class="abs" style="left:776px;top:326px" width="24" height="14" viewBox="0 0 24 14"><path d="M1 7h21M16 1l6 6-6 6" fill="none" stroke="var(--white)" stroke-width="2"/></svg>
  <div class="avatar" role="img" aria-label="Customer portrait" style="left:477px;top:305px;width:56px;height:56px;opacity:.7"></div>
  <div class="avatar" role="img" aria-label="Customer portrait" style="left:561px;top:295px;width:76px;height:76px"></div>
  <div class="avatar" role="img" aria-label="Customer portrait" style="left:665px;top:305px;width:56px;height:56px;opacity:.7"></div>
  <div class="abs" style="left:0;top:380px;width:1200px;text-align:center;color:var(--white);font-size:14px">- <b>Dana M.,</b> (Miami, FL) -</div>
  <div class="abs" style="left:0;top:400px;width:1200px;text-align:center;color:var(--orange);font-size:15px;letter-spacing:2px">★★★★☆</div>
  <div class="btn btn-ghost" style="left:469px;top:450px;width:262px;height:37px">Leave your reviews &amp; feedback</div>
</div>

<!-- Booking form -->
<div class="booking">
  <div class="booking-head">Contact us for<br>Booking</div>
  <div class="field" style="top:144px">Name</div>
  <div class="field" style="top:186px">Email</div>
  <div class="field" style="top:229px">Phone</div>
  <div class="field" style="top:270px">Service Requested <span style="float:right">⌄</span></div>
  <div class="field" style="top:313px;height:95px">Message</div>
  <div class="send"><svg width="12" height="12" viewBox="0 0 12 12"><path d="M0 6L12 0 9 12 6 7z" fill="var(--white)"/></svg>SEND</div>
</div>

<!-- Footer background -->
<svg class="abs" style="left:0;top:2700px" width="1200" height="543" viewBox="0 2700 1200 543">
  <defs><linearGradient id="footFill" x1="0" y1="0" x2="0" y2="1"><stop offset="0" stop-color="var(--footer-a)"/><stop offset="1" stop-color="var(--footer-b)"/></linearGradient></defs>
  <path d="M0 2790 C300 2700 600 2880 900 2800 S1150 2730 1200 2740 V3243 H0 Z" fill="url(#footFill)"/>
</svg>

<!-- Gallery -->
<h2 class="section-title" style="top:2503px">Photo Gallery</h2>
<div class="photo" role="img" aria-label="Photo of a rock waterfall pool" style="left:231px;background:linear-gradient(#4e6b3a,#2f8fb8)"></div>
<div class="photo" role="img" aria-label="Photo of a freeform backyard pool" style="left:484px;background:linear-gradient(#5d7184,#3a8fc3)"><svg class="abs" style="left:104px;top:103px" width="24" height="24" viewBox="0 0 24 24"><path d="M12 2v20M2 12h20" stroke="var(--white)" stroke-width="2"/></svg></div>
<div class="photo" role="img" aria-label="Photo of a pool with a gazebo and lawn" style="left:735px;background:linear-gradient(#5f7d46,#cfc9bb 60%,#3a9cc5)"></div>
<div class="abs dots" style="left:231px;top:2824px"><i></i><i class="on"></i><i></i><i></i><i></i><i></i></div>
<svg class="abs" style="left:930px;top:2848px" width="20" height="20" viewBox="0 0 20 20"><path d="M3 10l7-7 7 7M3 17l7-7 7 7" fill="none" stroke="var(--blue-light)" stroke-width="2"/></svg>

<!-- Footer content -->
<div class="abs footer-col" style="left:231px;top:2956px">
  <h4>Quick Link</h4>
  <ul><li>About Sunway Pool Care</li><li class="active">Services We Provide</li><li>Photo Gallery</li><li>Customers Reviews</li><li>Contact Us</li><li>Site Map</li></ul>
</div>
<div class="abs footer-col" style="left:484px;top:2956px">
  <h4>Service Territory</h4>
  <ul><li>Central Florida</li><li>Seminole</li><li>Orange Counties</li></ul>
</div>
<div class="abs footer-col" style="left:737px;top:2956px">
  <h4>Sunway Pool Care</h4>
  <ul>
    <li style="height:auto;line-height:1.55;margin-bottom:12px"><svg width="9" height="12" viewBox="0 0 9 12"><path d="M4.5 0a4.5 4.5 0 0 0-4.5 4.5C0 8 4.5 12 4.5 12S9 8 9 4.5A4.5 4.5 0 0 0 4.5 0z" fill="#e4e7eb"/></svg> Location:<br>1420 Harbor Palm Lane Lake Mary<br>Florida 32746</li>
    <li style="height:auto"><svg width="11" height="11" viewBox="0 0 24 24"><path d="M5 2c-2 2-2 6 2 11s9 8 11 7l3-3-4-4-3 2c-2-1-5-4-6-6l2-3-4-4z" fill="#e4e7eb"/></svg> Contact Us:</li>
    <li class="big" style="height:auto">407.555.0142</li>
    <li>E.: hello@sunwaypoolcare.example</li>
  </ul>
</div>
<div class="abs" style="left:231px;top:3172px;width:738px;height:1px;background:rgba(255,255,255,.3)"></div>
<div class="abs" style="left:231px;top:3197px;font-size:12px;color:#e4e7eb">Copyright © 2017 Sunway Pool Care</div>
<div class="abs social" style="left:736px;top:3190px"><span style="background:#c4c8cd"></span><span style="background:#c4c8cd"></span><span style="background:#c4c8cd"></span></div>

</body>
</html>
```